lunetra.com redesign

We are a successful web hosting company that has been around since 1999 with 10,000 customers managing 2,000 websites and 12,000 domain names. Our challenge - we are losing ground because our site is getting old, our pricing is not competitive and our feature set needs to change to match the new world of mobile centric everything. We want to reach out to all of the domain names that we don't host websites for. We believe that if we designed a new site that focuses on bringing home all of those externally hosted websites to our own web hosting company that we would have a solid future. We need to compete against mopwizzle.com, vantrimble.com, kerbloom.com, zinqhut.com, nolvark.com, brimfolk.com, quorvane.com, welbix.com and 100,000 others. We need to simplify our message with clean design, focused pages, easy decision making processes for the consumer. We use Billforge for the background provisioning and billing so we can pretty much manage any kind of pricing model and discounted promotion packages.
I would prefer Twitter bootstrap CSS based responsive design.

Reason: I was away on vacation for 2 weeks - I just got back - I need time to fairly review all submissions - thank you for your patience. Dorian Fenwick Lunetra.com

Thanks to all who submitted sample designs - unfortunately most of them were nothing much more than already available templates with some of my current content and logo added to them. I will try to be more specific to reduce the number of choices. I need the template be fully compatible with Billforge and Wordpress if you can't make it work with Billforge directly. Another question I have to ask is -"exactly what am I getting for my $500.00 - is it just a PSD template or actual integration of that theme into Billforge or Wordpress?"  I don't expect anyone to create new content for the site at that price. What do you charge if  you are able to create content or get directly involved in the site implementation of that template?

```html
<!DOCTYPE html>
<html lang="en">
<head>
<meta charset="utf-8">
<title>Lunetra – Hosting With Genuine Support</title>
<link rel="stylesheet" href="https://fonts.googleapis.com/css2?family=Open+Sans:wght@300;400;600;700&display=swap">
<style>
:root{
  --green:#5cae40;
  --green-dark:#4b9a33;
  --green-light:#70c052;
  --ink:#222;
  --ink-soft:#444;
  --line:#e4e4e4;
  --black:#111;
  --white:#fff;
  --nav-top:#fdfdfd;
  --nav-bottom:#ececec;
}
*{box-sizing:border-box;margin:0;padding:0}
html,body{width:1200px;height:2198px;overflow:hidden}
body{position:relative;background:var(--white);font-family:"Open Sans",Arial,sans-serif;color:var(--ink)}
.abs{position:absolute}

/* utility bar */
.util-bar{left:0;top:0;width:1200px;height:40px;background:#f6f6f6;border-bottom:1px solid var(--line)}
.util-links{left:160px;top:0;display:flex;height:40px}
.util-links span{font-size:12px;color:#555;padding:0 14px;line-height:40px;border-left:1px solid var(--line)}
.util-links span:last-child{border-right:1px solid var(--line)}
.util-social{left:896px;top:8px;display:flex;gap:8px}
.dot{width:24px;height:24px;border-radius:50%;background:var(--green)}

/* header */
.site-header{left:0;top:40px;width:1200px;height:134px;background:linear-gradient(var(--green-light),var(--green))}
.brand{left:172px;top:78px;font-size:56px;font-weight:700;color:var(--white);letter-spacing:-1px;line-height:1}
.field{background:var(--white);border:1px solid #ddd;font-size:12px;color:#999;padding:0 12px;display:flex;align-items:center}
.login-email{left:484px;top:90px;width:198px;height:36px}
.login-pass{left:692px;top:90px;width:200px;height:36px}
.login-btn{left:903px;top:90px;width:125px;height:36px;border:2px solid #d9f0cf;color:var(--white);font-size:16px;display:flex;align-items:center;justify-content:center;letter-spacing:1px}

/* nav */
.main-nav{left:0;top:174px;width:1200px;height:82px;background:linear-gradient(var(--nav-top),var(--nav-bottom));border-bottom:1px solid #ddd}
.nav-item{top:174px;height:82px;display:flex;align-items:center;justify-content:center;font-size:17px;color:#333;border-left:1px solid #ddd}
.nav-item.active{background:var(--white);border-bottom:3px solid var(--green)}

/* hero */
.hero{left:0;top:256px;width:1200px;height:495px;overflow:hidden}
.hero-photo{left:0;top:0;width:1200px;height:495px;background:linear-gradient(90deg,#c9b3a0 0%,#b8c4c2 35%,#dfe6e4 55%,#f1f3f2 75%,#cfd6d6 100%)}
.hero-veil{left:0;top:0;width:1200px;height:495px;background:linear-gradient(90deg,rgba(255,255,255,0) 40%,rgba(255,255,255,.55) 60%,rgba(255,255,255,.45) 100%)}
.slide-arrow{top:212px;width:77px;height:77px;border-radius:50%;border:3px solid var(--green);background:rgba(255,255,255,.85)}
.hero-title{left:592px;top:36px;font-size:55px;font-weight:300;line-height:64px;color:#222}
.hero-price{left:592px;top:184px;font-size:40px;color:var(--black)}
.hero-price b{font-size:56px;font-weight:700}
.hero-price sup{font-size:26px}
.hero-cta{left:595px;top:288px;width:330px;height:68px;background:var(--black);color:var(--white);font-size:29px;display:flex;align-items:center;justify-content:center}
.hero-note{left:596px;top:378px;font-size:40px;color:var(--green);line-height:1}
.hero-sub{left:597px;top:424px;font-size:24px;color:#333}
.slide-dots{left:540px;top:466px;display:flex;gap:8px}
.slide-dots i{width:10px;height:10px;border-radius:50%;background:rgba(255,255,255,.7)}

/* domain search */
.domain-bar{left:0;top:751px;width:1200px;height:97px;background:var(--black)}
.domain-lead{left:120px;top:770px;width:362px;text-align:right;color:var(--white);font-size:26px;line-height:31px}
.domain-lead strong{font-weight:700}
.domain-lead .price{color:var(--green-light);font-weight:700}
.domain-input{left:522px;top:784px;width:229px;height:39px}
.domain-tld{left:758px;top:784px;width:116px;height:39px;justify-content:space-between}
.domain-search{left:883px;top:784px;width:145px;height:39px;background:var(--green);color:var(--white);font-size:17px;display:flex;align-items:center;justify-content:center}

/* free services */
.section-title{left:0;top:898px;width:1200px;text-align:center;font-size:42px;font-weight:300;color:var(--green)}
.section-title b{font-weight:400}
.section-sub{left:0;top:952px;width:1200px;text-align:center;font-size:21px;color:#444}
.service{top:1005px;width:220px;text-align:center;font-size:25px;color:#222}
.service svg{display:block;margin:0 auto 18px}
.divider{left:0;width:1200px;height:1px;background:var(--line)}

/* premium */
.server-art{left:192px;top:1200px;width:275px;height:275px;background:linear-gradient(180deg,#5a5a5a,#1b1b1b 70%,#f3f3f3 100%);border-radius:4px}
.premium-title{left:507px;top:1188px;font-size:34px;color:var(--green)}
.premium-price{left:507px;top:1230px;font-size:40px;color:#222}
.premium-price b{font-weight:700}
.thumb{top:1304px;width:88px;height:88px;border-radius:50%;border:4px solid #333;background:radial-gradient(circle,#bbb,#555)}
.plan-btn{left:505px;top:1427px;width:228px;height:50px;background:var(--black);color:var(--white);font-size:26px;display:flex;align-items:center;justify-content:center}

/* features */
.feature{top:1535px;width:260px;text-align:center;font-size:25px;line-height:30px;color:#333}
.feature .badge{width:110px;height:110px;border-radius:50%;background:var(--green);margin:0 auto 32px;display:flex;align-items:center;justify-content:center}
.feature b{font-weight:400;color:var(--black);display:block}

/* footer */
.site-footer{left:0;top:1781px;width:1200px;height:340px;background:linear-gradient(var(--green-dark),var(--green))}
.foot-col{top:1816px;color:#e7f5e0}
.foot-col h4{font-size:25px;font-weight:400;color:var(--white);margin-bottom:18px}
.foot-col p{font-size:18px;line-height:34px}
.foot-social{left:172px;top:2073px;display:flex;gap:8px}
.foot-social .dot{background:var(--white)}
.legal-bar{left:0;top:2121px;width:1200px;height:77px;background:var(--white)}
.copyright{left:170px;top:2146px;font-size:17px;color:#222}
.powered{left:440px;top:2121px;width:317px;height:44px;background:var(--black);clip-path:polygon(0 0,100% 0,94% 100%,6% 100%);color:var(--white);font-size:18px;display:flex;align-items:center;justify-content:center;gap:8px}
.powered b{font-size:24px;font-weight:700}
.payments{left:777px;top:2138px;display:flex;gap:20px;font-size:20px;font-weight:700;color:#111}
</style>
</head>
<body>

<div class="abs util-bar"></div>
<nav class="abs util-links"><span>Company</span><span>Support</span><span>Partners</span><span>Pricing</span><span>Shopping Cart</span><span>Contact Us</span><span>References</span></nav>
<div class="abs util-social" aria-label="Social links"><i class="dot"></i><i class="dot"></i><i class="dot"></i><i class="dot"></i></div>

<header class="abs site-header"></header>
<div class="abs brand">lunetra</div>
<div class="abs field login-email">Enter Your E-mail</div>
<div class="abs field login-pass">Password</div>
<div class="abs login-btn">LOGIN</div>

<div class="abs main-nav"></div>
<div class="abs nav-item active" style="left:160px;width:78px">Home</div>
<div class="abs nav-item" style="left:238px;width:224px">Web Site Hosting Center</div>
<div class="abs nav-item" style="left:462px;width:223px">Domain Name Center</div>
<div class="abs nav-item" style="left:685px;width:139px">S.E.O. Toolkit</div>
<div class="abs nav-item" style="left:824px;width:101px">Support</div>
<div class="abs nav-item" style="left:925px;width:110px;border-right:1px solid #ddd">Client Area</div>

<section class="abs hero">
  <div class="abs hero-photo" role="img" aria-label="Smiling woman holding a tablet on a bright, softly blurred terrace"></div>
  <div class="abs hero-veil"></div>
  <svg class="abs slide-arrow" style="left:50px" viewBox="0 0 77 77"><path d="M44 22 L30 38.5 L44 55" fill="none" stroke="#5cae40" stroke-width="3"/></svg>
  <svg class="abs slide-arrow" style="left:1065px" viewBox="0 0 77 77"><path d="M33 22 L47 38.5 L33 55" fill="none" stroke="#5cae40" stroke-width="3"/></svg>
  <h1 class="abs hero-title">Hosting With<br>Genuine Support</h1>
  <div class="abs hero-price">only <b>$ 90 / year</b><sup>*</sup></div>
  <div class="abs hero-cta">Get Started Now</div>
  <div class="abs hero-note">no hidden fees</div>
  <div class="abs hero-sub">anytime money-back guarantee</div>
  <div class="abs slide-dots"><i></i><i></i><i></i></div>
</section>

<div class="abs domain-bar"></div>
<div class="abs domain-lead">Find Your <strong>DOMAIN</strong> Name<br>only <span class="price">$15/year.</span></div>
<div class="abs field domain-input">Enter Your Domain Name</div>
<div class="abs field domain-tld">.com <svg width="20" height="12" viewBox="0 0 20 12"><path d="M2 2 L10 10 L18 2" fill="none" stroke="#5cae40" stroke-width="2"/></svg></div>
<div class="abs domain-search">SEARCH</div>

<h2 class="abs section-title">Free <b>SERVICES</b></h2>
<p class="abs section-sub">Get These Free Services With All Accounts</p>

<div class="abs service" style="left:165px">
  <svg width="50" height="56" viewBox="0 0 50 56"><path d="M8 26 A17 17 0 0 1 38 14" fill="none" stroke="#5cae40" stroke-width="7"/><path d="M34 4 L44 16 L30 19 Z" fill="#5cae40"/><path d="M42 30 A17 17 0 0 1 12 42" fill="none" stroke="#5cae40" stroke-width="7"/><path d="M16 52 L6 40 L20 37 Z" fill="#5cae40"/></svg>
  Easy Transfer
</div>
<div class="abs service" style="left:376px">
  <svg width="50" height="56" viewBox="0 0 50 56"><path d="M8 10 L40 44" stroke="#5cae40" stroke-width="7"/><path d="M40 10 L12 40" stroke="#5cae40" stroke-width="6"/><circle cx="40" cy="10" r="8" fill="#5cae40"/><rect x="4" y="38" width="14" height="14" fill="#5cae40"/></svg>
  Site Builders
</div>
<div class="abs service" style="left:601px">
  <svg width="60" height="56" viewBox="0 0 60 56"><rect x="4" y="4" width="34" height="26" fill="none" stroke="#5cae40" stroke-width="3"/><rect x="22" y="22" width="34" height="26" fill="none" stroke="#5cae40" stroke-width="3"/><path d="M14 14 L38 36 M30 36 L38 36 L38 28" fill="none" stroke="#5cae40" stroke-width="3"/></svg>
  Site Installaro
</div>
<div class="abs service" style="left:824px">
  <svg width="50" height="56" viewBox="0 0 50 56"><circle cx="19" cy="19" r="13" fill="none" stroke="#5cae40" stroke-width="6"/><path d="M28 28 L44 46" stroke="#5cae40" stroke-width="8" stroke-linecap="round"/></svg>
  Be Found
</div>

<div class="abs divider" style="top:1160px"></div>

<div class="abs server-art" role="img" aria-label="Three black server towers standing in a row"></div>
<h3 class="abs premium-title" style="font-weight:400">Premium Business Hosting</h3>
<div class="abs premium-price">From <b>$ 90 / year</b></div>
<div class="abs thumb" style="left:507px" role="img" aria-label="Server rack close-up"></div>
<div class="abs thumb" style="left:636px" role="img" aria-label="Data centre aisle"></div>
<div class="abs thumb" style="left:769px" role="img" aria-label="Server cabinet"></div>
<div class="abs thumb" style="left:903px" role="img" aria-label="Globe on a server"></div>
<div class="abs plan-btn">E-lite Plan</div>

<div class="abs divider" style="top:1478px"></div>

<div class="abs feature" style="left:145px">
  <div class="badge"><svg width="56" height="62" viewBox="0 0 56 62"><path d="M28 4 L50 12 V30 C50 44 40 54 28 58 C16 54 6 44 6 30 V12 Z" fill="none" stroke="#fff" stroke-width="3.5"/><path d="M18 32 L26 40 L40 24" fill="none" stroke="#fff" stroke-width="4"/></svg></div>
  Secure Your<b>Domain Name</b>
</div>
<div class="abs feature" style="left:365px">
  <div class="badge"><svg width="60" height="50" viewBox="0 0 60 50"><rect x="6" y="32" width="8" height="14" fill="#fff"/><rect x="18" y="24" width="8" height="22" fill="#fff"/><rect x="30" y="18" width="8" height="28" fill="#fff"/><rect x="42" y="10" width="8" height="36" fill="#fff"/><path d="M4 26 L22 12 L32 18 L52 4" fill="none" stroke="#fff" stroke-width="3.5"/><path d="M44 2 L56 2 L56 14 Z" fill="#fff"/></svg></div>
  Market<b>Your Website</b>
</div>
<div class="abs feature" style="left:575px">
  <div class="badge"><svg width="58" height="46" viewBox="0 0 58 46"><rect x="4" y="4" width="22" height="38" rx="2" fill="#fff"/><rect x="32" y="4" width="22" height="38" rx="2" fill="#fff"/><path d="M9 13 H21 M9 20 H21 M9 27 H21 M37 13 H49 M37 20 H49 M37 27 H49" stroke="#5cae40" stroke-width="3"/></svg></div>
  Website<b>Hosting</b>
</div>
<div class="abs feature" style="left:797px">
  <div class="badge"><svg width="62" height="48" viewBox="0 0 62 48"><rect x="10" y="4" width="42" height="30" rx="2" fill="none" stroke="#fff" stroke-width="3.5"/><path d="M2 40 H60 L56 45 H6 Z" fill="#fff"/><circle cx="31" cy="19" r="6" fill="none" stroke="#fff" stroke-width="3"/><path d="M31 9 V12 M31 26 V29 M21 19 H24 M38 19 H41" stroke="#fff" stroke-width="3"/></svg></div>
  Effective<b>Web Development</b>
</div>

<footer class="abs site-footer"></footer>
<div class="abs foot-col" style="left:172px"><h4>About LUNETRA</h4><p>About Us<br>Legal<br>Blog</p></div>
<div class="abs foot-col" style="left:370px"><h4>Support</h4><p>Chat Tickets<br>Knowledge<br>Base System<br>Status</p></div>
<div class="abs foot-col" style="left:526px"><h4>Programs</h4><p>Affiliate<br>Seducation</p></div>
<div class="abs foot-col" style="left:683px"><h4>Products</h4><p>Shared Hosting<br>Vps Hosting<br>Dedicated Hosting<br>Reseller Hosting<br>Hosting Features</p></div>
<div class="abs foot-col" style="left:887px"><h4>Company</h4><p>Associates<br>Terms Of Service<br>About<br>Privacy Policy<br>Contact</p></div>
<div class="abs foot-social" aria-label="Social links"><i class="dot"></i><i class="dot"></i><i class="dot"></i><i class="dot"></i></div>

<div class="abs legal-bar"></div>
<div class="abs copyright">©2014 Lunetra. All rights reserved</div>
<div class="abs powered">Powered By : <b>Billforge</b></div>
<div class="abs payments"><span>Paywell</span><span>Vistra</span><span>Orbcard</span><span>Grandline</span></div>

</body>
</html>
```